Hockey Youth Club - Complete HP Design

I need a complete homepage design for a new youth hockey club. There are already some elements that can be used. For more information, please visit this products webpage. This site is currently unavailable for purchase at this time (Current) -) Team (Players, Coaches, Crew) -) Club (Philiosophy , Rules, Management Board, ....) -) Partners (Sponsors, Partners, ...)) Contact (Contact details, Callback Button) -) Shop (in the beginning view of products - further planned as online shop ) -) .... probably 2-3 more -) Footer with social media info, ..... Homepages from other youth hockey clubs (ex. Www.brel. At - this is what I am looking for in my life - BUT we dont want to copy them !!! Im interested in new and innovative designs.
Updates

Project Deadline Extended
Reason: Too much Wordpress - no innovation - please offer more designs in dark concept. At the moment the design is too decent - we are looking for sporty, active and fresh design. Thank you

Target Market(s)

Youth Hockey Players Parents

Industry/Entity Type

Club

Number of Pages Required

5+ page

Colors
fbed38
9d9d9d
1b1b1b
f5f5f5
ffffff

Requirements
Must have
• Clearline, modern design,
Nice to have
• Flashing elements (maybe the scratches fading in ...)
Should not have
• chaos

```html
<!DOCTYPE html>
<html lang="en">
<head>
<meta charset="utf-8">
<title>Blazers Youth Hockey Club</title>
<link rel="stylesheet" href="https://fonts.googleapis.com/css2?family=Khand:wght@500;600;700&family=Open+Sans:wght@400;600;700&display=swap">
<style>
:root{
  --yellow:#fbed38;
  --yellow-deep:#e9d620;
  --grey:#9d9d9d;
  --ink:#1b1b1b;
  --ice:#f5f5f5;
  --white:#ffffff;
  --line:#d9d9d9;
}
*{box-sizing:border-box;margin:0;padding:0}
html,body{width:1200px;height:3243px;overflow:hidden;background:var(--white)}
body{position:relative;font-family:"Open Sans",Arial,sans-serif;color:var(--ink)}
.head-font{font-family:"Khand","Arial Narrow",sans-serif;font-weight:700;text-transform:uppercase}
a{color:inherit;text-decoration:none}

/* hero */
.hero{position:absolute;left:0;top:0;width:1200px;height:710px;
  background:radial-gradient(ellipse at 60% 40%,#fbfbfb 0%,#e9ecee 55%,#d8dcdf 100%)}
.nav{position:absolute;top:30px;left:604px;display:flex;gap:10px}
.nav a{font-family:"Open Sans",Arial,sans-serif;font-size:13px;font-weight:700;text-transform:uppercase;padding:6px 10px;color:var(--ink)}
.nav a.active{background:var(--yellow);border:1px solid #c9b900}
.brand{position:absolute;display:flex;align-items:center;gap:10px}
.brand-mark{width:34px;height:34px;border-radius:50%;background:var(--ink)}
.brand-name{font-family:"Khand","Arial Narrow",sans-serif;font-weight:700;font-size:44px;color:var(--ink);text-transform:uppercase;letter-spacing:1px}
.hero .brand{left:130px;top:110px}
.hero-title{position:absolute;left:236px;top:292px}
.hero-title .pre{font-size:40px;line-height:1}
.hero-title .main{font-size:66px;line-height:1;margin-top:8px}
.btn-hero{position:absolute;left:238px;top:431px;width:122px;height:42px;background:var(--yellow);border:2px solid var(--ink);
  display:flex;align-items:center;justify-content:center;gap:8px;font-family:"Khand",sans-serif;font-weight:700;font-size:17px}
.hero-photo{position:absolute;left:450px;top:110px;width:590px;height:590px;
  background:radial-gradient(ellipse at 48% 40%,#e2512c 0%,#b33a22 28%,#3a3f55 52%,rgba(200,205,210,0) 72%)}

/* shared */
.wrap{position:absolute;left:130px;width:940px}
.section-title{text-align:center;font-size:34px;line-height:1}
.section-title::after{content:"";display:block;width:112px;height:4px;background:var(--yellow);margin:8px auto 0}
.btn-small{display:inline-block;background:var(--yellow);font-size:11px;font-weight:700;text-transform:uppercase;padding:5px 10px;border:1px solid #c9b900}

/* news */
.news-head{position:absolute;left:0;width:1200px;top:770px;display:flex;justify-content:center;align-items:center;gap:82px}
.news-grid{top:871px;display:grid;grid-template-columns:repeat(4,227px);gap:10px}
.news-card{height:296px;border:1px solid var(--line);padding:24px 26px}
.news-date{display:inline-block;font-family:"Khand",sans-serif;font-weight:600;font-size:12px;color:#8a7e00;border:1px solid var(--yellow-deep);padding:1px 6px}
.news-card h3{font-size:17px;line-height:1.1;margin:20px 0 14px}
.news-card p{font-size:11.5px;line-height:1.7;margin-bottom:18px}
.tiles{top:1183px;display:grid;grid-template-columns:repeat(4,227px);gap:10px}
.tile{height:175px;background:var(--yellow-deep);display:flex;flex-direction:column;align-items:center;justify-content:center;gap:14px}
.tile span{font-size:25px}

/* team */
.team-title{top:1428px}
.tabs{position:absolute;top:1516px;left:0;width:1200px;display:flex;justify-content:center;gap:40px;font-size:12px;font-weight:700;text-transform:uppercase}
.tabs .on{color:#c9b400}
.team-grid{top:1593px;display:grid;grid-template-columns:repeat(4,1fr);text-align:center}
.player-photo{width:184px;height:184px;border-radius:50%;margin:0 auto}
.player h4{font-size:19px;margin:40px 0 10px}
.player p{font-size:12px;line-height:1.6;width:200px;margin:0 auto 20px}

/* shop */
.shop-title{top:2038px}
.shop-grid{top:2140px;display:grid;grid-template-columns:repeat(4,1fr);text-align:center}
.product-photo{width:200px;height:238px;margin:0 auto}
.product h4{font-size:19px;margin-top:24px}

/* partners */
.partners-title{top:2512px}
.partners{position:absolute;top:2622px;left:210px;width:750px;display:flex;justify-content:space-between;align-items:center}
.badge{width:64px;height:64px;background:#c8c8c8}
.badge.round{border-radius:50%}

/* footer */
.footer{position:absolute;left:0;top:2789px;width:1200px;height:454px;
  background:radial-gradient(ellipse at 50% 30%,#fafafa 0%,#e6e9eb 60%,#d6dadd 100%)}
.footer .brand{left:500px;top:78px}
.footer h5{font-family:"Khand",sans-serif;font-weight:700;font-size:15px;text-transform:uppercase;margin-bottom:16px}
.f-menu{position:absolute;left:130px;top:160px;font-size:12.5px;line-height:1.6}
.f-contact{position:absolute;left:264px;top:160px;font-size:12.5px;line-height:1.6}
.f-contact li{display:flex;gap:16px;margin-bottom:14px;list-style:none}
.f-menu ul{list-style:none}
.f-follow{position:absolute;left:500px;top:245px;width:200px;text-align:center}
.socials{display:flex;justify-content:center;gap:22px}
.socials span{width:20px;height:20px;border-radius:50%;background:var(--ink)}
.f-news{position:absolute;left:778px;top:170px;width:292px}
.f-input{height:47px;background:var(--white);font-size:13px;padding:14px 16px;color:#555}
.f-btn{display:inline-block;margin-top:18px;background:var(--yellow);border:1px solid #c9b900;font-family:"Khand",sans-serif;font-weight:700;font-size:15px;padding:4px 16px}
.f-rule{position:absolute;left:463px;top:384px;width:274px;height:1px;background:#bbb}
.copy{position:absolute;left:0;width:1200px;top:404px;text-align:center;font-size:12px}
</style>
</head>
<body>

<header class="hero">
  <nav class="nav">
    <a class="active">Home</a><a>News</a><a>Team</a><a>Club</a><a>Partners</a><a>Shop</a><a>Contact</a>
  </nav>
  <div class="brand"><span class="brand-mark"></span><span class="brand-name">Blazers</span></div>
  <div class="hero-photo" role="img" aria-label="Youth hockey player in red jersey skating with stick and puck"></div>
  <h1 class="hero-title head-font"><div class="pre">Welcome to</div><div class="main">Our Blazers Site</div></h1>
  <a class="btn-hero">READ MORE
    <svg width="10" height="14" viewBox="0 0 10 14"><path d="M2 1l6 6-6 6" fill="none" stroke="#1b1b1b" stroke-width="2"/></svg></a>
</header>

<div class="news-head">
  <svg width="22" height="44" viewBox="0 0 22 44"><path d="M20 2L2 22l18 20" fill="none" stroke="#9d9d9d" stroke-width="2"/></svg>
  <h2 class="section-title head-font">Latest News</h2>
  <svg width="22" height="44" viewBox="0 0 22 44"><path d="M2 2l18 20L2 42" fill="none" stroke="#9d9d9d" stroke-width="2"/></svg>
</div>

<section class="wrap news-grid">
  <article class="news-card"><span class="news-date">20 July,2017</span><h3 class="head-font">Making this the first true generator</h3><p>Handful of model sentence structures, to generate Lorem Ipsum which looks reasonable. The generated Lorem Ipsum is therefore.</p><a class="btn-small">Read more</a></article>
  <article class="news-card"><span class="news-date">20 July,2017</span><h3 class="head-font">Embarrassing hidden in the middle of text</h3><p>Handful of model sentence structures, to generate Lorem Ipsum which looks reasonable. The generated Lorem Ipsum is therefore.</p><a class="btn-small">Read more</a></article>
  <article class="news-card"><span class="news-date">20 July,2017</span><h3 class="head-font">From repetition, injected humour, or non</h3><p>Handful of model sentence structures, to generate Lorem Ipsum which looks reasonable. The generated Lorem Ipsum is therefore.</p><a class="btn-small">Read more</a></article>
  <article class="news-card"><span class="news-date">20 July,2017</span><h3 class="head-font">Lorem Ipsum is simply dummy text</h3><p>Handful of model sentence structures, to generate Lorem Ipsum which looks reasonable. The generated Lorem Ipsum is therefore.</p><a class="btn-small">Read more</a></article>
</section>

<section class="wrap tiles">
  <div class="tile"><svg width="44" height="50" viewBox="0 0 44 50" fill="none" stroke="#1b1b1b" stroke-width="2"><path d="M4 2h22l10 10v34H4z"/><path d="M26 2v10h10"/><circle cx="32" cy="38" r="8" fill="#e9d620"/><path d="M32 35v7M32 32v1"/></svg><span class="head-font">Info's</span></div>
  <div class="tile"><svg width="50" height="50" viewBox="0 0 50 50" fill="none" stroke="#1b1b1b" stroke-width="2"><path d="M10 4l24 34h8M40 4L16 38H8"/><ellipse cx="25" cy="44" rx="7" ry="3"/></svg><span class="head-font">Rules</span></div>
  <div class="tile"><svg width="46" height="46" viewBox="0 0 46 46" fill="none" stroke="#1b1b1b" stroke-width="2"><path d="M10 4l7 9-4 5c3 6 8 11 14 14l5-4 9 7-5 6C20 40 6 26 4 10z"/><path d="M28 4a14 14 0 0 1 14 14M28 11a7 7 0 0 1 7 7"/></svg><span class="head-font">Call Us</span></div>
  <div class="tile"><svg width="54" height="40" viewBox="0 0 54 40" fill="none" stroke="#1b1b1b" stroke-width="2"><rect x="2" y="2" width="50" height="36"/><path d="M2 2l25 20L52 2"/></svg><span class="head-font">E Mail Us</span></div>
</section>

<h2 class="wrap section-title head-font team-title">Our Team</h2>
<div class="tabs"><span class="on">Players</span><span>Coaches</span><span>Crew</span></div>
<section class="wrap team-grid">
  <div class="player"><div class="player-photo" role="img" aria-label="Hockey player in white kit" style="background:radial-gradient(circle,#c9cdd0,#7d8184)"></div><h4 class="head-font">Aron Miles</h4><p>Handful of model sentence structures, to generate Lorem Ipsum which looks reasonab.</p><a class="btn-small">Read more</a></div>
  <div class="player"><div class="player-photo" role="img" aria-label="Hockey player in red kit" style="background:radial-gradient(circle,#c23a3a,#2c2f3a)"></div><h4 class="head-font">Aron Miles</h4><p>Handful of model sentence structures, to generate Lorem Ipsum which looks reasonab.</p><a class="btn-small">Read more</a></div>
  <div class="player"><div class="player-photo" role="img" aria-label="Field hockey player on green pitch" style="background:radial-gradient(circle,#5d9a4f,#2f6b3a)"></div><h4 class="head-font">Aron Miles</h4><p>Handful of model sentence structures, to generate Lorem Ipsum which looks reasonab.</p><a class="btn-small">Read more</a></div>
  <div class="player"><div class="player-photo" role="img" aria-label="Young goalie in helmet" style="background:radial-gradient(circle,#3f6f9a,#1e2733)"></div><h4 class="head-font">Aron Miles</h4><p>Handful of model sentence structures, to generate Lorem Ipsum which looks reasonab.</p><a class="btn-small">Read more</a></div>
</section>

<h2 class="wrap section-title head-font shop-title">Shop</h2>
<section class="wrap shop-grid">
  <div class="product"><div class="product-photo" role="img" aria-label="Yellow T-shirt" style="background:linear-gradient(#f6d23a,#e0b81c)"></div><h4 class="head-font">T Shirt 1</h4></div>
  <div class="product"><div class="product-photo" role="img" aria-label="Grey T-shirt" style="background:linear-gradient(#a8a8a8,#8a8a8a)"></div><h4 class="head-font">T Shirt 2</h4></div>
  <div class="product"><div class="product-photo" role="img" aria-label="Navy and grey zip jacket" style="background:linear-gradient(90deg,#2e3a52,#b9bcc0 40%,#b9bcc0 60%,#2e3a52)"></div><h4 class="head-font">T Shirt 3</h4></div>
  <div class="product"><div class="product-photo" role="img" aria-label="Red T-shirt with white stripes" style="background:linear-gradient(#d0424a,#b52f38)"></div><h4 class="head-font">T Shirt 4</h4></div>
</section>

<h2 class="wrap section-title head-font partners-title">Partners</h2>
<div class="partners">
  <span class="badge round"></span><span class="badge"></span><span class="badge round"></span><span class="badge round"></span><span class="badge"></span><span class="badge round"></span>
</div>

<footer class="footer">
  <div class="brand"><span class="brand-mark"></span><span class="brand-name">Blazers</span></div>
  <div class="f-menu"><h5>Menu</h5><ul><li>Home</li><li>Team</li><li>Club</li><li>Partners</li><li>Shop</li><li>Contact</li></ul></div>
  <div class="f-contact"><h5>Contact Us</h5>
    <ul>
      <li><svg width="10" height="14" viewBox="0 0 10 14"><path d="M5 0a5 5 0 0 0-5 5c0 4 5 9 5 9s5-5 5-9a5 5 0 0 0-5-5z" fill="#1b1b1b"/><circle cx="5" cy="5" r="2" fill="#f5f5f5"/></svg><span>482 Harbor Lane<br>Easton, ST 20417</span></li>
      <li><svg width="12" height="12" viewBox="0 0 12 12"><path d="M2 0l3 3-1.5 2c1 2 2 3 3.5 3.5L9 7l3 3-2 2C5 12 0 7 0 2z" fill="#1b1b1b"/></svg><span>555.XXX.0142</span></li>
      <li><svg width="12" height="10" viewBox="0 0 12 10"><rect width="12" height="10" fill="#1b1b1b"/><path d="M0 0l6 5 6-5" stroke="#f5f5f5" fill="none"/></svg><span>info@blazers.club</span></li>
    </ul></div>
  <div class="f-follow"><h5>Follow Us</h5><div class="socials"><span aria-label="social link"></span><span aria-label="social link"></span><span aria-label="social link"></span><span aria-label="social link"></span></div></div>
  <div class="f-news"><h5>Newsletter Signup</h5><div class="f-input">Email Address</div><a class="f-btn">SIGNUP</a></div>
  <div class="f-rule"></div>
  <p class="copy">Copyrights @ blazers.club.2017 All Rights reserved</p>
</footer>

</body>
</html>
```